Political Mail Out Quintero front and back

Front
Esteban (9th Grade) Quintero!

What's that famous saying?

Show me who your friends are and I'll tell you who you really are!
(show the two guys)

Walter Cuellar is charged with voter fraud by changing voter addresses from across the RGV so they could vote in Edinburg
Back
Did Esteban (9th Grade) Quintero commit voter fraud when he ran for office in 2016?
(insert blurred photo)

Here is a list of people from all over the RGV that voted in Edinburg in the 2016 race.
Here is a break down:

(highlight the number and where they were first registered to vote)

9 People voted in Edinburg who were registered in Donna.
13 People voted in Edinburg who were registered in San Juan
8 People voted in Edinburg who were registered in Pharr
31 People voted in Edinburg who were registered in McAllen
2 People voted in Edinburg who were registered in La Joya
6 People voted in Edinburg who were registered in Edcouch
2 People voted in Edinburg who were registered in Mercedes
2 People voted in Edinburg who were registered in Monte Alto
6 People voted in Edinburg who were registered in Weslaco
1 Person voted in Edinburg who were registered in Penitas
3 People voted in Edinburg who were registered in Alamo
5 People voted in Edinburg who were registered in Elsa
6 People voted in Edinburg who were registered in Mission
1 Person voted in Edinburg who were registered in Alton

Will Esteban (9th Grade) Quintero CHEAT in 2020?

Only time will tell.

Vote Esteban (9th Grade) Quintero OUT of office.

```html
<!DOCTYPE html>
<html lang="en">
<head>
<meta charset="utf-8">
<title>Quintero Mail Out — Front and Back</title>
<link rel="stylesheet" href="https://fonts.googleapis.com/css2?family=Arvo:wght@700&family=Teko:wght@500&family=Roboto+Condensed:wght@700&family=Arimo:ital,wght@0,700;1,700&family=Bebas+Neue&display=swap">
<style>
  :root{
    --page:#e6e3de;
    --blue-deep:#1c2f6e;
    --blue:#2e4a9a;
    --red-deep:#9a0f12;
    --red:#c81b1e;
    --accent-red:#e3262b;
    --white:#ffffff;
    --dark:#1d1d1f;
    --dark-2:#3a3a3d;
    --silver:#d9d9db;
  }
  *{margin:0;padding:0;box-sizing:border-box}
  html,body{width:1200px;height:888px;overflow:hidden;background:var(--page)}
  .canvas{position:relative;width:1200px;height:888px}
  .card{position:absolute;top:115px;height:658px;overflow:hidden;
    background:radial-gradient(circle at 50% 45%,var(--blue) 0%,var(--blue-deep) 75%);
    box-shadow:0 4px 14px rgba(0,0,0,.35)}
  .card--front{left:69px;width:507px}
  .card--back{left:630px;width:509px}
  .layer{position:absolute;left:0;top:0}
  .headline{position:absolute;left:0;width:100%;text-align:center;color:var(--white);
    font-family:"Arvo",serif;font-size:37px;line-height:1;text-transform:uppercase;
    text-shadow:0 2px 2px rgba(0,0,0,.5)}
  .tagline{position:absolute;left:0;width:100%;text-align:center;top:118px;
    font-family:"Teko",sans-serif;font-size:42px;line-height:1;color:var(--accent-red);text-transform:uppercase}
  .photo-friends{position:absolute;left:0;top:170px;width:345px;height:300px;
    background:linear-gradient(160deg,#6d7aa8 0%,#a88a78 45%,#7a7a7c 100%)}
  .saying{position:absolute;right:12px;top:198px;text-align:right;
    font-family:"Roboto Condensed",sans-serif;font-size:23px;line-height:31px}
  .saying__lead{color:var(--accent-red)}
  .saying__punch{color:var(--white);text-transform:uppercase}
  .charge{position:absolute;left:0;width:100%;top:476px;text-align:center;color:var(--white);
    font-family:"Roboto Condensed",sans-serif;font-size:25px;line-height:35px}
  .band{position:absolute;left:0;width:100%;background:linear-gradient(var(--dark-2),var(--dark));
    border-top:3px solid var(--silver);border-bottom:3px solid var(--silver);text-align:center;color:var(--white)}
  .band--front{top:592px;height:52px;font-family:"Arimo",sans-serif;font-style:italic;font-size:22px;line-height:46px;color:#f2e6e6}
  .question{position:absolute;left:25px;top:24px;width:330px;color:var(--white);
    font-family:"Roboto Condensed",sans-serif;font-size:29px;line-height:36px}
  .photo-roster{position:absolute;right:0;top:0;width:149px;height:215px;
    background:linear-gradient(180deg,#f2f2f2 0%,#dcdcdc 60%,#c9c9c9 100%)}
  .intro{position:absolute;left:22px;top:253px;width:470px;color:var(--white);
    font-family:"Arimo",sans-serif;font-size:13.5px;line-height:16px}
  .breakdown-tab{position:absolute;left:0;top:293px;width:195px;height:25px}
  .breakdown-tab span{position:absolute;left:22px;top:3px;color:var(--white);
    font-family:"Roboto Condensed",sans-serif;font-size:15px}
  .tally{position:absolute;left:22px;top:330px;list-style:none;color:var(--white);
    font-family:"Arimo",sans-serif;font-size:10px;line-height:15.3px}
  .tally b{font-style:italic}
  .tally strong{font-weight:700}
  .tally span{font-weight:400}
  .band--back{top:556px;height:48px;font-family:"Arimo",sans-serif;line-height:19px;padding-top:3px}
  .band--back .band__ask{font-style:italic;font-size:15px}
  .band--back .band__answer{font-size:17px;letter-spacing:1px;text-transform:uppercase}
  .call-out{position:absolute;left:0;width:100%;top:614px;text-align:center;color:var(--white);
    font-family:"Bebas Neue",sans-serif;font-size:30px;line-height:1}
</style>
</head>
<body>
<main class="canvas">

  <section class="card card--front" aria-label="Front">
    <h1 class="headline" style="top:26px">Esteban (9th Grade)</h1>
    <h1 class="headline" style="top:74px">Quintero!</h1>
    <p class="tagline">What's that famous saying?</p>

    <div class="photo-friends" role="img" aria-label="Photo of the two men standing together, smiling"></div>

    <svg class="layer" width="507" height="658" viewBox="0 0 507 658" aria-hidden="true">
      <defs>
        <linearGradient id="redFront" x1="0" y1="0" x2="0" y2="1">
          <stop offset="0" stop-color="#d2201f"/><stop offset="1" stop-color="#9a0f12"/>
        </linearGradient>
        <linearGradient id="circleFill" x1="0" y1="0" x2="0" y2="1">
          <stop offset="0" stop-color="#3a3a3d"/><stop offset="1" stop-color="#161618"/>
        </linearGradient>
      </defs>
      <circle cx="420" cy="295" r="130" fill="url(#circleFill)" stroke="#d9d9db" stroke-width="4"/>
      <polygon points="0,382 172,452 507,338 507,658 0,658" fill="#ffffff"/>
      <polygon points="0,392 172,462 507,348 507,658 0,658" fill="url(#redFront)"/>
    </svg>

    <p class="saying">
      <span class="saying__lead">Show me who<br>your friends<br>are and</span><br>
      <span class="saying__punch">I'll tell you<br>who you really<br>are!</span>
    </p>

    <p class="charge">Walter Cuellar is charged with voter<br>fraud by changing voter addresses<br>from across the RGV</p>
    <p class="band band--front">so they could vote in Edinburg</p>
  </section>

  <section class="card card--back" aria-label="Back">
    <h2 class="question">Did Esteban (9th Grade) Quintero commit voter fraud when he ran for office in 2016?</h2>
    <div class="photo-roster" role="img" aria-label="Blurred photo of a voter roll printout"></div>

    <svg class="layer" width="509" height="658" viewBox="0 0 509 658" aria-hidden="true">
      <defs>
        <linearGradient id="redBack" x1="0" y1="0" x2="0" y2="1">
          <stop offset="0" stop-color="#c81b1e"/><stop offset="1" stop-color="#a31214"/>
        </linearGradient>
      </defs>
      <polygon points="0,168 200,240 509,178 509,190 200,252 0,180" fill="#ffffff"/>
      <polygon points="0,180 200,252 509,190 509,658 0,658" fill="url(#redBack)"/>
      <polygon points="0,178 200,250 509,188 509,191 200,253 0,181" fill="#bfbfc2"/>
    </svg>

    <p class="intro">Here is a list of people from all over the RGV that voted in Edinburg in the 2016 race.</p>

    <div class="breakdown-tab">
      <svg width="195" height="25" viewBox="0 0 195 25" aria-hidden="true">
        <polygon points="0,0 180,0 195,12.5 180,25 0,25" fill="#2b2b2e" stroke="#d9d9db" stroke-width="1.5"/>
      </svg>
      <span>Here is a break down:</span>
    </div>

    <ul class="tally">
      <li><b>9</b> <span>People voted in Edinburg who were registered in</span> <strong>Donna</strong></li>
      <li><b>13</b> <span>People voted in Edinburg who were registered in</span> <strong>San Juan</strong></li>
      <li><b>8</b> <span>People voted in Edinburg who were registered in</span> <strong>Pharr</strong></li>
      <li><b>31</b> <span>People voted in Edinburg who were registered in</span> <strong>McAllen</strong></li>
      <li><b>2</b> <span>People voted in Edinburg who were registered in</span> <strong>La Joya</strong></li>
      <li><b>6</b> <span>People voted in Edinburg who were registered in</span> <strong>Edcouch</strong></li>
      <li><b>2</b> <span>People voted in Edinburg who were registered in</span> <strong>Mercedes</strong></li>
      <li><b>2</b> <span>People voted in Edinburg who were registered in</span> <strong>Monte Alto</strong></li>
      <li><b>6</b> <span>People voted in Edinburg who were registered in</span> <strong>Weslaco</strong></li>
      <li><b>1</b> <span>Person voted in Edinburg who were registered in</span> <strong>Penitas</strong></li>
      <li><b>3</b> <span>People voted in Edinburg who were registered in</span> <strong>Alamo</strong></li>
      <li><b>5</b> <span>People voted in Edinburg who were registered in</span> <strong>Elsa</strong></li>
      <li><b>6</b> <span>People voted in Edinburg who were registered in</span> <strong>Mission</strong></li>
      <li><b>1</b> <span>Person voted in Edinburg who were registered in</span> <strong>Alton</strong></li>
    </ul>

    <div class="band band--back">
      <p class="band__ask">Will Esteban (9th Grade) Quintero CHEAT in 2020?</p>
      <p class="band__answer">Only time will tell.</p>
    </div>

    <p class="call-out">Vote Esteban (9th Grade) Quintero out of office.</p>
  </section>

</main>
</body>
</html>
```